iOS7 test prep app

I need 3 basic screens and 2 product images for an iOS7 app I am prototyping. I provided lots of detail in the attached brief. This is an education product, so warm colors (especially reds) work best.

If you've done flat design for mobile products, please take a look ... Thanks!

Greetings, all. Thank you for your submissions. I am meeting with my product development team this week to review your submissions, and will select a designer before the end of the week. I appreciate your patience with my process, and thank you again for your interest in my project. I'll be back to you soon ... -Dorian

```html
<!DOCTYPE html>
<html lang="en">
<head>
<meta charset="utf-8">
<title>Cortexa Dashboard Styles</title>
<link rel="stylesheet" href="https://fonts.googleapis.com/css2?family=Roboto+Condensed:wght@300;400;700&family=Roboto:wght@400&display=swap">
<style>
:root{
  --canvas:#e9e4f6;
  --shadow:#aea8b9;
  --title:#2f2f33;
  --orange-top:#f3a517;
  --orange-bottom:#ee870f;
  --orange:#f0920f;
  --panel-dark:#1c1c1c;
  --panel-light:#ffffff;
  --screen-light:#e4e4e4;
  --meter-red:#d10f2b;
  --gauge:#222222;
  --white:#ffffff;
  --ink:#1d1d1d;
  --muted:#6b6b6b;
  --yellow:#f6c400;
  --amber:#f08a12;
  --red:#e0202a;
  --green:#20ad20;
  --blue:#1e8fe4;
  --pie-blue:#1e90e6;
  --pie-green:#1fb51f;
  --pie-yellow:#f5c800;
  --pie-orange:#f08c12;
  --pie-red:#e8242e;
  --pie-red-deep:#d0102a;
  --pie-crimson:#b0123e;
  --pie-purple:#8a1fc4;
}
*{box-sizing:border-box;margin:0;padding:0}
html,body{width:1200px;height:1000px;overflow:hidden}
body{background:var(--canvas);position:relative;font-family:"Roboto Condensed",sans-serif}
.backdrop{position:absolute;left:0;top:0}
.style-title{position:absolute;top:30px;width:480px;text-align:center;font-size:40px;font-weight:400;color:var(--title)}
.phone{position:absolute;top:118px;width:480px;height:852px;overflow:hidden}
.phone--dark{left:106px;background:linear-gradient(var(--orange-top),var(--orange-bottom))}
.phone--light{left:619px;background:var(--screen-light)}
.status-bar{position:absolute;left:0;top:0;width:100%;height:32px;color:var(--white);font-family:"Roboto",sans-serif;font-size:17px}
.status-bar .carrier{position:absolute;left:10px;top:7px;display:flex;align-items:center;gap:4px}
.status-bar .dots{letter-spacing:-1px;font-size:12px}
.status-bar .time{position:absolute;left:0;width:100%;top:7px;text-align:center}
.status-bar .battery{position:absolute;right:8px;top:7px;display:flex;align-items:center;gap:6px}
.battery-icon{width:34px;height:14px;border:1.5px solid var(--white);border-radius:3px;padding:1px}
.battery-icon span{display:block;width:100%;height:100%;background:var(--white);border-radius:1px}
.app-header{position:absolute;left:0;top:32px;width:100%}
.phone--dark .app-header{height:70px}
.brand{position:absolute;left:17px;top:12px;font-size:36px;font-weight:700;color:var(--white)}
.header-icons{position:absolute;right:14px;top:18px;display:flex;gap:26px}
.phone--light .app-header{height:64px;background:linear-gradient(var(--orange-top),var(--orange-bottom));box-shadow:0 2px 3px rgba(0,0,0,.15)}
.app-title{text-align:center;line-height:64px;font-size:23px;font-weight:400;color:var(--white)}
.panel{position:absolute;overflow:hidden}
.phone--dark .panel{background:var(--panel-dark);color:var(--white)}
.phone--light .panel{background:var(--panel-light);color:var(--ink);border:1px solid #d4d4d4}
.phone--dark .panel--meter{background:var(--meter-red)}
.phone .panel--plan{background:var(--panel-light);color:var(--ink)}
.panel--stats{left:16px;top:114px;width:217px;height:182px}
.panel--meter{left:248px;top:114px;width:217px;height:182px}
.panel--booster{left:16px;top:313px;width:217px;height:183px}
.panel--plan{left:248px;top:313px;width:217px;height:183px}
.panel--trending{left:16px;top:513px;width:449px;height:183px}
.panel-heading{position:absolute;top:8px;width:100%;text-align:center;font-size:21px;font-weight:400;text-transform:uppercase}
.rows{position:absolute;left:0;top:46px;width:100%;list-style:none}
.row{position:relative;height:34px;font-size:19px;font-weight:400}
.phone--light .row{font-weight:300;color:var(--muted)}
.row .label{position:absolute;left:15px;top:5px}
.row .value{position:absolute;top:5px}
.panel--stats .value{right:16px;color:var(--white)}
.phone--light .panel--stats .value{color:var(--ink)}
.row .arrow{position:absolute;top:4px;width:16px;height:24px}
.panel--stats .arrow{right:16px}
.panel--booster .value{left:100px}
.panel--booster .arrow{left:185px}
.phone--light .panel--booster .value{color:var(--ink)}
.trend-col{position:absolute;top:46px;width:224px;list-style:none}
.trend-col--left{left:0}
.trend-col--right{left:217px}
.panel--trending .value{left:118px}
.panel--trending .arrow{left:185px}
.up{color:var(--red)}
.down{color:var(--green)}
.tone-yellow{color:var(--yellow)!important}
.phone--light .tone-yellow{color:var(--amber)!important}
.tone-red{color:var(--red)!important}
.tone-green{color:var(--green)!important}
.meter{position:absolute;left:0;top:0}
.begin-test{position:absolute;left:42px;top:743px;width:396px;height:65px;display:flex;align-items:center;justify-content:center;font-size:27px;font-weight:400;color:var(--white);text-transform:uppercase}
.phone--dark .begin-test{border:2px solid var(--white)}
.phone--light .begin-test{background:linear-gradient(var(--orange-top),var(--orange-bottom))}
.plan-chart{position:absolute;left:0;top:0}
</style>
</head>
<body>
<svg class="backdrop" width="1200" height="1000" aria-hidden="true">
  <polygon points="586,118 616,118 1200,702 1200,1000 616,1000 586,970" fill="var(--shadow)"/>
  <polygon points="1099,118 1200,219 1200,1000 1129,1000 1099,970" fill="var(--shadow)"/>
</svg>
<svg width="0" height="0" style="position:absolute" aria-hidden="true">
  <symbol id="arrow-up" viewBox="0 0 16 24"><path d="M8 23V3M1.5 9.5L8 3l6.5 6.5" fill="none" stroke="currentColor" stroke-width="1.6"/></symbol>
  <symbol id="arrow-down" viewBox="0 0 16 24"><path d="M8 1v20M1.5 14.5L8 21l6.5-6.5" fill="none" stroke="currentColor" stroke-width="1.6"/></symbol>
  <symbol id="plan-pie" viewBox="0 0 217 183">
    <g transform="rotate(-90 108 108)" fill="none" stroke-width="57">
      <circle cx="108" cy="108" r="28.5" pathLength="100" stroke="var(--pie-blue)" stroke-dasharray="14 86" stroke-dashoffset="0"/>
      <circle cx="108" cy="108" r="28.5" pathLength="100" stroke="var(--pie-green)" stroke-dasharray="20 80" stroke-dashoffset="-14"/>
      <circle cx="108" cy="108" r="28.5" pathLength="100" stroke="var(--pie-yellow)" stroke-dasharray="12 88" stroke-dashoffset="-34"/>
      <circle cx="108" cy="108" r="28.5" pathLength="100" stroke="var(--pie-orange)" stroke-dasharray="15 85" stroke-dashoffset="-46"/>
      <circle cx="108" cy="108" r="28.5" pathLength="100" stroke="var(--pie-red)" stroke-dasharray="9 91" stroke-dashoffset="-61"/>
      <circle cx="108" cy="108" r="28.5" pathLength="100" stroke="var(--pie-red-deep)" stroke-dasharray="9 91" stroke-dashoffset="-70"/>
      <circle cx="108" cy="108" r="28.5" pathLength="100" stroke="var(--pie-crimson)" stroke-dasharray="9 91" stroke-dashoffset="-79"/>
      <circle cx="108" cy="108" r="28.5" pathLength="100" stroke="var(--pie-purple)" stroke-dasharray="12 88" stroke-dashoffset="-88"/>
    </g>
    <g font-family="Roboto Condensed, sans-serif" font-size="11" fill="#fff" text-anchor="middle" dominant-baseline="middle">
      <text x="125" y="73">14%</text><text x="145" y="106">20%</text><text x="130" y="139">12%</text>
      <text x="100" y="145">15%</text><text x="77" y="129">9%</text><text x="71" y="109">9%</text>
      <text x="76" y="89">9%</text><text x="94" y="73">12%</text>
    </g>
    <g font-family="Roboto Condensed, sans-serif" font-size="13" dominant-baseline="middle">
      <text x="7" y="61" fill="var(--pie-purple)">S&amp;IC</text>
      <text x="7" y="95" fill="var(--pie-crimson)">HP&amp;M</text>
      <text x="7" y="130" fill="var(--pie-red-deep)">PI</text>
      <text x="7" y="163" fill="var(--pie-red-deep)">BC&amp;C</text>
      <text x="210" y="61" text-anchor="end" fill="var(--pie-blue)">PA</text>
      <text x="210" y="95" text-anchor="end" fill="var(--pie-green)">MC</text>
      <text x="210" y="130" text-anchor="end" fill="var(--pie-yellow)">RRP</text>
      <text x="210" y="163" text-anchor="end" fill="var(--pie-orange)">P&amp;PT</text>
    </g>
  </symbol>
</svg>

<h2 class="style-title" style="left:107px">Dashboard Style 1</h2>
<h2 class="style-title" style="left:613px">Dashboard Style 2</h2>

<!-- Dark style -->
<section class="phone phone--dark">
  <div class="status-bar">
    <span class="carrier"><span class="dots">●●●○○</span> Vantel
      <svg width="18" height="13" viewBox="0 0 18 13"><path d="M1 4.5a11 11 0 0 1 16 0M3.8 7.3a7 7 0 0 1 10.4 0M6.6 10a3 3 0 0 1 4.8 0" fill="none" stroke="#fff" stroke-width="1.8"/></svg></span>
    <span class="time">7:28 PM</span>
    <span class="battery">100% <span class="battery-icon"><span></span></span></span>
  </div>
  <header class="app-header">
    <div class="brand">Cortexa</div>
    <div class="header-icons">
      <svg width="38" height="38" viewBox="0 0 38 38"><circle cx="19" cy="19" r="17" fill="none" stroke="#fff" stroke-width="1.8"/><text x="19" y="26" text-anchor="middle" font-family="Roboto, sans-serif" font-size="20" fill="#fff">?</text></svg>
      <svg width="38" height="38" viewBox="0 0 38 38"><g fill="none" stroke="#fff" stroke-width="1.8"><circle cx="19" cy="19" r="11"/><circle cx="19" cy="19" r="5"/><path d="M19 2v6M19 30v6M2 19h6M30 19h6M7 7l4.2 4.2M26.8 26.8L31 31M7 31l4.2-4.2M26.8 11.2L31 7"/></g></svg>
    </div>
  </header>

  <article class="panel panel--stats">
    <h3 class="panel-heading">Key Stats</h3>
    <ul class="rows">
      <li class="row"><span class="label">Total Tests:</span><span class="value">6</span></li>
      <li class="row"><span class="label">Last Score:</span><span class="value tone-yellow">68%</span></li>
      <li class="row"><span class="label">Cum. Score:</span><span class="value tone-red">59%</span></li>
      <li class="row"><span class="label">Trend:</span><svg class="arrow tone-green"><use href="#arrow-up"/></svg></li>
    </ul>
  </article>

  <article class="panel panel--meter">
    <h3 class="panel-heading">Readiness Meter</h3>
    <svg class="meter" width="217" height="182" viewBox="0 0 217 182">
      <text x="108" y="74" text-anchor="middle" font-family="Roboto Condensed, sans-serif" font-weight="300" font-size="34" fill="#fff">65%</text>
      <path d="M27.3 137.9A88 88 0 0 1 192.7 137.9L132.6 159.8A24 24 0 0 0 87.4 159.8Z" fill="var(--gauge)"/>
      <circle cx="110" cy="168" r="18" fill="#8c0a22"/>
      <path d="M101 166L121 104L119 168Z" fill="#fff"/>
      <circle cx="110" cy="166" r="10" fill="#fff"/>
      <text x="16" y="176" font-family="Roboto Condensed, sans-serif" font-size="12" fill="#fff">NOT READY</text>
      <text x="200" y="176" text-anchor="end" font-family="Roboto Condensed, sans-serif" font-size="12" fill="#fff">READY</text>
    </svg>
  </article>

  <article class="panel panel--booster">
    <h3 class="panel-heading">Booster Levels</h3>
    <ul class="rows">
      <li class="row"><span class="label">HP</span><span class="value">5x</span><svg class="arrow up"><use href="#arrow-up"/></svg></li>
      <li class="row"><span class="label">PI</span><span class="value">5x</span><svg class="arrow up"><use href="#arrow-up"/></svg></li>
      <li class="row"><span class="label">PA</span><span class="value">4x</span><svg class="arrow down"><use href="#arrow-down"/></svg></li>
      <li class="row"><span class="label">CM</span><span class="value">3x</span><svg class="arrow down"><use href="#arrow-down"/></svg></li>
    </ul>
  </article>

  <article class="panel panel--plan">
    <h3 class="panel-heading" style="font-size:20px">Test Plan Distribution</h3>
    <svg class="plan-chart" width="217" height="183"><use href="#plan-pie"/></svg>
  </article>

  <article class="panel panel--trending">
    <h3 class="panel-heading">Trending Performance by Category</h3>
    <ul class="trend-col trend-col--left">
      <li class="row"><span class="label">Care Mgt</span><span class="value tone-yellow">68%</span><svg class="arrow tone-red"><use href="#arrow-down"/></svg></li>
      <li class="row"><span class="label">Safety IC</span><span class="value tone-yellow">68%</span><svg class="arrow tone-green"><use href="#arrow-up"/></svg></li>
      <li class="row"><span class="label">HP &amp; M</span><span class="value tone-red">59%</span><svg class="arrow tone-green"><use href="#arrow-up"/></svg></li>
      <li class="row"><span class="label">PI</span><span class="value tone-red">44%</span><svg class="arrow tone-red"><use href="#arrow-down"/></svg></li>
    </ul>
    <ul class="trend-col trend-col--right">
      <li class="row"><span class="label">Basic C &amp; C</span><span class="value tone-green">77%</span><svg class="arrow tone-red"><use href="#arrow-down"/></svg></li>
      <li class="row"><span class="label">Pharma PT</span><span class="value tone-yellow">67%</span><svg class="arrow tone-green"><use href="#arrow-up"/></svg></li>
      <li class="row"><span class="label">Risk</span><span class="value tone-yellow">58%</span><svg class="arrow tone-green"><use href="#arrow-up"/></svg></li>
      <li class="row"><span class="label">PA</span><span class="value tone-red">43%</span><svg class="arrow tone-red"><use href="#arrow-down"/></svg></li>
    </ul>
  </article>

  <div class="begin-test">Begin Test</div>
</section>

<!-- Light style -->
<section class="phone phone--light">
  <div class="status-bar" style="background:var(--orange-top)">
    <span class="carrier"><span class="dots">●●●○○</span> Vantel
      <svg width="18" height="13" viewBox="0 0 18 13"><path d="M1 4.5a11 11 0 0 1 16 0M3.8 7.3a7 7 0 0 1 10.4 0M6.6 10a3 3 0 0 1 4.8 0" fill="none" stroke="#fff" stroke-width="1.8"/></svg></span>
    <span class="time">7:28 PM</span>
    <span class="battery">100% <span class="battery-icon"><span></span></span></span>
  </div>
  <header class="app-header">
    <div class="app-title">Cortexa Mobile Exam Prep</div>
  </header>

  <article class="panel panel--stats">
    <h3 class="panel-heading">Key Stats</h3>
    <ul class="rows">
      <li class="row"><span class="label">Total Tests:</span><span class="value">6</span></li>
      <li class="row"><span class="label">Last Score:</span><span class="value tone-yellow">68%</span></li>
      <li class="row"><span class="label">Cum. Score:</span><span class="value tone-red">59%</span></li>
      <li class="row"><span class="label">Trend:</span><svg class="arrow tone-green"><use href="#arrow-up"/></svg></li>
    </ul>
  </article>

  <article class="panel panel--meter">
    <h3 class="panel-heading">Readiness Meter</h3>
    <svg class="meter" width="217" height="182" viewBox="0 0 217 182">
      <text x="108" y="74" text-anchor="middle" font-family="Roboto Condensed, sans-serif" font-weight="300" font-size="34" fill="var(--blue)">65%</text>
      <path d="M27.3 137.9A88 88 0 0 1 192.7 137.9L132.6 159.8A24 24 0 0 0 87.4 159.8Z" fill="var(--gauge)"/>
      <circle cx="110" cy="166" r="14" fill="none" stroke="var(--blue)" stroke-width="6"/>
      <path d="M101 166L121 104L119 168Z" fill="#c9c9c9"/>
      <circle cx="110" cy="166" r="9" fill="#c9c9c9"/>
      <text x="16" y="176" font-family="Roboto Condensed, sans-serif" font-size="12" fill="var(--muted)">NOT READY</text>
      <text x="200" y="176" text-anchor="end" font-family="Roboto Condensed, sans-serif" font-size="12" fill="var(--muted)">READY</text>
    </svg>
  </article>

  <article class="panel panel--booster">
    <h3 class="panel-heading">Booster Levels</h3>
    <ul class="rows">
      <li class="row"><span class="label">HP</span><span class="value">5x</span><svg class="arrow up"><use href="#arrow-up"/></svg></li>
      <li class="row"><span class="label">PI</span><span class="value">5x</span><svg class="arrow up"><use href="#arrow-up"/></svg></li>
      <li class="row"><span class="label">PA</span><span class="value">4x</span><svg class="arrow down"><use href="#arrow-down"/></svg></li>
      <li class="row"><span class="label">CM</span><span class="value">3x</span><svg class="arrow down"><use href="#arrow-down"/></svg></li>
    </ul>
  </article>

  <article class="panel panel--plan">
    <h3 class="panel-heading" style="font-size:20px">Test Plan Distribution</h3>
    <svg class="plan-chart" width="217" height="183"><use href="#plan-pie"/></svg>
  </article>

  <article class="panel panel--trending">
    <h3 class="panel-heading">Trending Performance by Category</h3>
    <ul class="trend-col trend-col--left">
      <li class="row"><span class="label">Care Mgt</span><span class="value tone-yellow">68%</span><svg class="arrow tone-red"><use href="#arrow-down"/></svg></li>
      <li class="row"><span class="label">Safety IC</span><span class="value tone-yellow">68%</span><svg class="arrow tone-green"><use href="#arrow-up"/></svg></li>
      <li class="row"><span class="label">HP &amp; M</span><span class="value tone-red">59%</span><svg class="arrow tone-green"><use href="#arrow-up"/></svg></li>
      <li class="row"><span class="label">PI</span><span class="value tone-red">44%</span><svg class="arrow tone-red"><use href="#arrow-down"/></svg></li>
    </ul>
    <ul class="trend-col trend-col--right">
      <li class="row"><span class="label">Basic C &amp; C</span><span class="value tone-green">77%</span><svg class="arrow tone-red"><use href="#arrow-down"/></svg></li>
      <li class="row"><span class="label">Pharma PT</span><span class="value tone-yellow">67%</span><svg class="arrow tone-green"><use href="#arrow-up"/></svg></li>
      <li class="row"><span class="label">Risk</span><span class="value tone-yellow">58%</span><svg class="arrow tone-green"><use href="#arrow-up"/></svg></li>
      <li class="row"><span class="label">PA</span><span class="value tone-red">43%</span><svg class="arrow tone-red"><use href="#arrow-down"/></svg></li>
    </ul>
  </article>

  <div class="begin-test">Begin Test</div>
</section>
</body>
</html>
```